Math Help Website Needs New Design

Looking to refresh the design of my existing site (brightsumguide.net) to be easier on the eyes. I am fully capable of doing the HTML coding and have for years, but I don't have the eye for good design, colors, layout, and fonts. This is where I need help!

I need both a new design scheme and a new logo that matches. The overall functionality will be the same as the existing site, and should not be unrecognizable.

Target Market(s)

It should appeal to students (age 13-22) and their parents, so it should NOT be childish in appearance, nor should it be corporate.

Requirements
Must have
• Should be simple, easy-to-navigate, and neither childish nor corporate. I am looking for a design for both the homepage and a similar "content" page. Simple, bold colors are preferred. A logo should be prominent at the top, with a search bar nearby. Below that I need a similar navigational area like I already have. Then, I need about 200px wide ad space on the left of the main body area.

```html
<!DOCTYPE html>
<html lang="en">
<head>
<meta charset="utf-8">
<title>BrightSum Guide – Math Help</title>
<link href="https://fonts.googleapis.com/css2?family=Alfa+Slab+One&family=Arimo:wght@400;700&display=swap" rel="stylesheet">
<style>
:root{
  --navy:#1d2a5c;
  --sky:#6f93bf;
  --body-blue:#2f4f9c;
  --body-blue-deep:#24408a;
  --panel:#ffffff;
  --ink:#2b3a86;
  --heading:#55638f;
  --btn:#4a5a8f;
  --muted:#7a7a7a;
  --orange:#f39a1e;
  --yellow:#ffde00;
  --green:#8cc63f;
  --teal:#2aa6d5;
  --tab-orange:#f7941d;
  --red:#ee1c24;
  --ad:#c9c9c9;
  --line:#9fb4d6;
}
*{box-sizing:border-box;margin:0;padding:0}
html,body{width:998px;height:1200px;overflow:hidden}
body{position:relative;font-family:"Arimo",Arial,sans-serif;background:var(--sky);color:var(--ink)}
.abs{position:absolute}
a{color:inherit;text-decoration:none}

.topbar{left:0;top:0;width:998px;height:22px;background:var(--navy)}
.topbar a{position:absolute;left:791px;top:4px;color:#fff;font-weight:700;font-size:12px}

.header{left:0;top:22px;width:998px;height:154px;background:var(--sky)}
.brand{left:96px;top:95px;display:flex;align-items:center;gap:8px;color:#fff;font-weight:700;font-size:26px;letter-spacing:.5px}
.brand i{display:block;width:18px;height:18px;border-radius:50%;background:#fff}
.search{left:730px;top:64px;width:173px;height:24px;border-radius:3px;background:#b8cbe2;border:1px solid #d6e2f0;font-size:10px;color:#fff;padding:6px 0 0 13px}
.search svg{position:absolute;right:5px;top:4px}

.tab{top:113px;height:32px;color:#fff;font-weight:700;font-size:12px;display:flex;align-items:center;justify-content:center;border-radius:6px 6px 0 0;transform:skewX(6deg)}
.tab span,.tab svg{transform:skewX(-6deg)}
.tab-home{left:385px;width:62px;background:var(--yellow)}
.tab-text{left:450px;width:116px;background:var(--green)}
.tab-video{left:568px;width:116px;background:var(--teal)}
.tab-more{left:686px;width:121px;background:var(--tab-orange)}
.tab-forum{left:809px;width:83px;background:var(--red)}
.navbar{left:246px;top:145px;width:660px;height:31px;background:var(--yellow);border-radius:3px 3px 0 0}

.stage{left:0;top:176px;width:998px;height:739px;background:radial-gradient(ellipse at 50% 45%,var(--body-blue) 0%,var(--body-blue-deep) 100%)}

.ad{background:var(--ad);border:4px solid #fff;color:#fff;display:flex;align-items:center;justify-content:center}
.ad span{font-size:34px;transform:rotate(-90deg);white-space:nowrap;letter-spacing:1px}
.ad-tall{left:92px;top:193px;width:140px;height:495px}
.ad-short{left:92px;top:703px;width:140px;height:186px}

.photo{background:linear-gradient(180deg,#9bb3d3,#6f8fbd);border-radius:4px}

.panel{background:var(--panel);border-radius:3px}
.panel-main{left:246px;top:176px;width:660px;height:517px;border-radius:0 0 4px 4px}
.panel-ask{left:246px;top:714px;width:658px;height:177px}

.h{font-family:"Alfa Slab One",Georgia,serif;color:var(--heading);letter-spacing:1.5px;font-size:20px;font-weight:400;white-space:nowrap}
.lesson-img{width:191px;height:73px;border-radius:4px}
.lesson-label{font-family:"Alfa Slab One",Georgia,serif;color:var(--heading);font-size:12.5px;letter-spacing:1px;white-space:nowrap}
.more{width:51px;height:14px;background:var(--btn);border-radius:3px;color:#fff;font-size:9px;display:flex;align-items:center;justify-content:center;gap:3px}

.news{left:260px;top:547px;width:183px;list-style:none}
.news li{height:29.5px;border-bottom:1px solid var(--line);font-size:11px;padding-top:9px;padding-left:6px}
.news li:last-child{border-bottom:none}

.post h4{font-size:11px;font-weight:400;color:var(--ink);line-height:13px}
.post .by{font-size:11px;color:var(--orange);line-height:13px}
.post p{font-size:9px;color:var(--muted);line-height:12px}

.bubble-text{left:263px;top:683px;width:195px;text-align:center;color:#fff;font-family:"Alfa Slab One",Georgia,serif;font-size:13px;letter-spacing:1.5px;line-height:19px}

.ask-intro{left:481px;top:740px;width:190px;font-size:10.5px;color:var(--muted);line-height:13px}
.field-label{font-size:10.5px;color:var(--muted)}
.field{width:121px;height:20px;border:1px solid #9aa3c5;border-radius:4px;background:#f4f4f6}
.question{left:690px;top:727px;width:192px;height:122px;border:1px solid #b8c0d8;border-radius:4px;background:#f5f5f5}
.btn{height:14px;background:var(--btn);border-radius:3px;color:#fff;font-size:9.5px;display:flex;align-items:center;justify-content:center;gap:4px}

.footer{left:0;top:915px;width:998px;height:220px;background:var(--sky)}
.col{top:935px;color:#fff;font-size:13.5px}
.col h5{font-size:13.5px;font-weight:400;margin-bottom:5px}
.col li{list-style:none;line-height:21.2px}
.divider{top:938px;width:1px;height:183px;background:#e6edf6}

.bottombar{left:0;top:1135px;width:998px;height:65px;background:var(--navy);color:#fff;font-size:12px}
.legal{left:109px;top:9px}
.copy{left:658px;top:9px}
</style>
</head>
<body>

<div class="abs topbar"><a href="#">REGISTER / SIGN IN</a></div>

<header class="abs header"></header>
<div class="abs brand"><i></i>brightsumguide</div>
<div class="abs search">Search the site...
  <svg width="14" height="14" viewBox="0 0 14 14"><circle cx="8" cy="6" r="4.5" fill="none" stroke="#fff" stroke-width="1.6"/><line x1="4.6" y1="9.4" x2="1" y2="13" stroke="#fff" stroke-width="2"/></svg>
</div>

<nav>
  <a class="abs tab tab-home" href="#" aria-label="Home"><svg width="20" height="18" viewBox="0 0 20 18"><path d="M10 1 L19 9 H16 V17 H12 V12 H8 V17 H4 V9 H1 Z" fill="#fff"/></svg></a>
  <a class="abs tab tab-text" href="#"><span>TEXT LESSONS</span></a>
  <a class="abs tab tab-video" href="#"><span>VIDEO LESSONS</span></a>
  <a class="abs tab tab-more" href="#"><span>MORE SUBJECTS</span></a>
  <a class="abs tab tab-forum" href="#"><span>FORUM</span></a>
</nav>
<div class="abs navbar"></div>

<div class="abs stage"></div>

<aside class="abs ad ad-tall"><span>ADVERTISEMENT</span></aside>
<aside class="abs ad ad-short"><span>AD</span></aside>

<div class="abs photo" role="img" aria-label="Photo of a student peeking around the panel edge" style="left:906px;top:200px;width:92px;height:190px;border-radius:0 4px 4px 0"></div>

<main class="abs panel panel-main"></main>
<h2 class="abs h" style="left:265px;top:187px">MATH LESSONS</h2>

<div class="abs lesson-img" role="img" aria-label="Pencil on handwritten algebra" style="left:264px;top:235px;background:linear-gradient(135deg,#f2f2f2,#c9c9c9)"></div>
<div class="abs lesson-label" style="left:265px;top:316px">ALGEBRA</div>
<a class="abs more" href="#" style="left:403px;top:318px">MORE <b>❯</b></a>

<div class="abs lesson-img" role="img" aria-label="Compass and pen on graph paper" style="left:478px;top:235px;background:linear-gradient(135deg,#ffffff,#bfc3c8)"></div>
<div class="abs lesson-label" style="left:479px;top:316px">GEOMETRY</div>
<a class="abs more" href="#" style="left:616px;top:318px">MORE <b>❯</b></a>

<div class="abs lesson-img" role="img" aria-label="Chalkboard with trigonometry graphs" style="left:687px;top:235px;background:linear-gradient(135deg,#555,#222)"></div>
<div class="abs lesson-label" style="left:688px;top:316px">TRIGONOMETRY</div>
<a class="abs more" href="#" style="left:826px;top:318px">MORE <b>❯</b></a>

<div class="abs lesson-img" role="img" aria-label="Hand writing calculus on paper" style="left:264px;top:350px;background:linear-gradient(135deg,#eee,#b9b4ae)"></div>
<div class="abs lesson-label" style="left:265px;top:431px">CALCULUS</div>
<a class="abs more" href="#" style="left:403px;top:432px">MORE <b>❯</b></a>

<div class="abs lesson-img" role="img" aria-label="Pen over a printed bar chart" style="left:478px;top:350px;background:linear-gradient(135deg,#f5f5f5,#cfd6c8)"></div>
<div class="abs lesson-label" style="left:479px;top:431px">STATISTICS</div>
<a class="abs more" href="#" style="left:616px;top:432px">MORE <b>❯</b></a>

<div class="abs lesson-img" role="img" aria-label="Baseball stadium with crowd" style="left:687px;top:350px;background:linear-gradient(180deg,#b77a6a,#4f8a3c 55%,#a43a3a)"></div>
<div class="abs lesson-label" style="left:688px;top:431px">SPORTS MATH</div>
<a class="abs more" href="#" style="left:826px;top:432px">MORE <b>❯</b></a>

<h2 class="abs h" style="left:263px;top:505px">WHAT'S NEW</h2>
<ul class="abs news">
  <li>Multiplying Polynomials</li>
  <li>Derivative of an Inverse Function</li>
  <li>Derivatives of Logs and Exps</li>
  <li>Differentiating Trig Functions</li>
</ul>

<h2 class="abs h" style="left:480px;top:505px">CURRENT DISCUSSIONS</h2>
<svg class="abs" style="left:479px;top:550px" width="62" height="56" viewBox="0 0 62 56">
  <path d="M4 3 H60 V47 H50 L58 56 L38 47 H4 Z" fill="var(--orange)"/>
  <path d="M0 0 H57 V44 H47 L54 52 L35 44 H0 Z" fill="var(--btn)"/>
  <text x="28" y="22" fill="#fff" font-size="14" text-anchor="middle" font-family="Arimo, sans-serif">12 Jan</text>
</svg>
<div class="abs post" style="left:548px;top:547px;width:330px">
  <h4>Comparing Likert scales of different lengths</h4>
  <div class="by">Posted by: Statlearner</div>
  <p>Hi there math and statistics experts! For my thesis I am doing research about listener's attitudes towards 4 different Dutch accents.</p>
</div>
<svg class="abs" style="left:479px;top:617px" width="62" height="56" viewBox="0 0 62 56">
  <path d="M4 3 H60 V47 H50 L58 56 L38 47 H4 Z" fill="var(--orange)"/>
  <path d="M0 0 H57 V44 H47 L54 52 L35 44 H0 Z" fill="var(--btn)"/>
  <text x="28" y="22" fill="#fff" font-size="14" text-anchor="middle" font-family="Arimo, sans-serif">6 Jan</text>
</svg>
<div class="abs post" style="left:548px;top:611px;width:330px">
  <h4>Time/dist/speed.</h4>
  <div class="by">Posted by: MapleGrove</div>
  <p>a, b and c are three linear towns. c divides the line. It takes Ron 72 mins to travel from a to c. It takes Zak 50 mins to travel from b to c.</p>
</div>

<section class="abs panel panel-ask"></section>
<div class="abs photo" role="img" aria-label="Photo of a student lying down writing in a notebook" style="left:260px;top:730px;width:205px;height:185px"></div>
<svg class="abs" style="left:263px;top:679px" width="196" height="80" viewBox="0 0 196 80">
  <path d="M3 0 H193 Q196 0 196 3 V47 Q196 50 193 50 H70 L72 78 L40 50 H3 Q0 50 0 47 V3 Q0 0 3 0 Z" fill="var(--orange)"/>
</svg>
<div class="abs bubble-text">ASK YOUR QUESTION<br>MESSAGE BOARD</div>

<p class="abs ask-intro">Register and Sign in to get your questions answered by our friendly Forum volunteers.</p>
<span class="abs field-label" style="left:481px;top:804px">User Name:</span>
<div class="abs field" style="left:544px;top:802px"></div>
<span class="abs field-label" style="left:481px;top:829px">Password:</span>
<div class="abs field" style="left:544px;top:827px"></div>
<a class="abs btn" href="#" style="left:483px;top:858px;width:65px">SIGN IN <b>❯</b></a>
<a class="abs btn" href="#" style="left:590px;top:858px;width:74px">REGISTER <b>❯</b></a>
<div class="abs question"></div>
<a class="abs btn" href="#" style="left:692px;top:858px;width:137px">SUMBIT YOUR QUESTION <b>❯</b></a>

<footer class="abs footer"></footer>
<div class="abs col" style="left:265px">
  <h5>FREE MATH RESOURCES</h5>
  <ul><li>Mr. Alvaro's Lessons</li><li>Algebra Lessons</li><li>Geometry Lessons</li><li>Trigonometry Lessons</li><li>Calculus Lessons</li><li>Statistics Lessons</li><li>Sports Math</li></ul>
</div>
<div class="abs divider" style="left:468px"></div>
<div class="abs col" style="left:493px">
  <h5>FREE CALCULATORS HELP</h5>
  <ul><li>Equation Solver</li><li>Equation Grapher</li><li>Derivative Calculator</li><li>Factoring Calculator</li><li>Integral Calculator</li></ul>
</div>
<div class="abs divider" style="left:696px"></div>
<div class="abs col" style="left:720px">
  <h5>MORE SUBJECTS</h5>
  <ul><li>Ask an Expert</li><li>Books</li><li>Calculator Buying Guide</li><li>Famous Mathematicialns</li><li>Origins of Math</li><li>Math Games</li><li>Glossary</li><li>Study Tips</li></ul>
</div>

<div class="abs bottombar">
  <div class="abs legal">Terms of Use &nbsp;|&nbsp; Privacy Policy &nbsp;|&nbsp; Contact Us &nbsp;|&nbsp; About Us &nbsp;|&nbsp; Download PDF Viewer</div>
  <div class="abs copy">BrightSum Guide © 2013 All Rights Reserved</div>
</div>

</body>
</html>
```